Exterior cleaning company requires a eye catching a5 leaflet

we need some updated leaflet designs, a5 folded, we are targeting all exterior cleaning contracts, including roof cleaning & treatment, render cleaning & Treatment, driveways, block paving cleaning using the latest in low pressure cleaning technologies along side high pressure jetwashing. gutter clearance and flushing, water fed telescopic pole window cleaning of difficult to reach windows and high buildings. our website : www.tkbellowsec.co.uk facebook page: https://www.facebook.com/tkbellowsexteriorcareltd Instagram: https://www.instagram.com/tkbellowsec/ a quick google search of roof cleaning, soft washing etc will provide results of what we are doing

Target Market(s)

home owners, commercial clients

Font styles to use
Serif
Sans Serif

Requirements
Must have
• A5 Landscape folded leaflet, front page with company information and bullet points of main works : window & conservatory cleaning, roof cleaning & treatment, Render cleaning & treatment, pressure washing, soft washing, gutter clearing, pressure washing of patios, driveways, gutters, fascias (more info can be provided on techniques etc if required)

```html
<!DOCTYPE html>
<html lang="en">
<head>
<meta charset="utf-8">
<title>TK Bellows Window Cleaning – Leaflet</title>
<link rel="stylesheet" href="https://fonts.googleapis.com/css2?family=Bebas+Neue&family=Didact+Gothic&display=swap">
<style>
  :root {
    --frame-grey: #8e8f8e;
    --text-grey: #878887;
    --title-grey: #8a8b8a;
    --paper: #ffffff;
  }
  html, body {
    margin: 0;
    padding: 0;
    overflow: hidden;
    background: var(--paper);
  }
  .leaflet {
    position: relative;
    width: 1200px;
    height: 927px;
    overflow: hidden;
    background: var(--paper);
    font-family: "Didact Gothic", "Helvetica Neue", Arial, sans-serif;
    color: var(--text-grey);
  }
  .frame-top {
    position: absolute;
    left: 0; top: 0;
    width: 1200px; height: 78px;
    background: var(--frame-grey);
  }
  .frame-right {
    position: absolute;
    left: 1130px; top: 0;
    width: 70px; height: 927px;
    background: var(--frame-grey);
  }
  .photo {
    position: absolute;
    border-radius: 50%;
    border: 0;
  }
  .photo--window {
    left: 47px; top: -53px;
    width: 608px; height: 608px;
    background: linear-gradient(160deg, #cfd3d6 0%, #6f7a6a 35%, #4a4f4c 55%, #c9b39a 80%, #d8c4aa 100%);
  }
  .photo--roof {
    left: 681px; top: 177px;
    width: 426px; height: 426px;
    background: linear-gradient(180deg, #c6c9cc 0%, #8d9190 28%, #b9bcbb 45%, #d4d6d4 100%);
  }
  .intro {
    position: absolute;
    left: 49px; top: 580px;
    width: 330px;
    margin: 0;
    font-size: 24px;
    line-height: 38.7px;
    letter-spacing: 0.5px;
  }
  .offer {
    position: absolute;
    left: 449px; top: 580px;
    width: 320px;
    margin: 0;
    font-size: 22.5px;
    line-height: 35px;
    letter-spacing: 0.6px;
  }
  .phone {
    position: absolute;
    left: 449px; top: 700px;
    margin: 0;
    font-family: "Bebas Neue", "Oswald", sans-serif;
    font-size: 44px;
    line-height: 1;
    letter-spacing: 0.5px;
    color: var(--text-grey);
  }
  .social {
    position: absolute;
    left: 449px; top: 771px;
    margin: 0; padding: 0;
    list-style: none;
  }
  .social__item {
    display: flex;
    align-items: center;
    height: 46px;
    margin-bottom: 9px;
  }
  .social__dot {
    width: 46px; height: 46px;
    border-radius: 50%;
    background: var(--text-grey);
    flex: none;
  }
  .social__handle {
    margin-left: 8px;
    font-size: 17px;
    letter-spacing: 0.4px;
    color: var(--text-grey);
  }
  .brand {
    position: absolute;
    left: 828px; top: 652px;
    margin: 0;
    font-family: "Bebas Neue", "Oswald", sans-serif;
    font-weight: 400;
    font-size: 70px;
    line-height: 64px;
    letter-spacing: 1px;
    color: var(--title-grey);
  }
  .tagline {
    position: absolute;
    left: 829px; top: 864px;
    margin: 0;
    font-size: 17px;
    letter-spacing: 0.6px;
    color: var(--text-grey);
  }
</style>
</head>
<body>
  <main class="leaflet">
    <div class="frame-top"></div>
    <div class="frame-right"></div>

    <div class="photo photo--window" role="img" aria-label="Photo: a cleaner using a water-fed telescopic pole on a large glass-walled building beside a stone patio"></div>
    <div class="photo photo--roof" role="img" aria-label="Photo: a worker in hi-vis and a harness pressure washing a corrugated metal roof"></div>

    <p class="intro">We are a professional, friendly and reliable window cleaning company with a wide range of services to offer from gutter cleaning to patio and drive way cleaning !</p>

    <p class="offer">Has your render gone dirty? Is it an eye sore ? Give us a call for your free quote.</p>

    <p class="phone">01632 960 481</p>

    <ul class="social">
      <li class="social__item"><span class="social__dot"></span><span class="social__handle">@tkbellowsexteriorcareltd</span></li>
      <li class="social__item"><span class="social__dot"></span><span class="social__handle">@tkbellowsec</span></li>
    </ul>

    <h1 class="brand">TK Bellows<br>Window<br>Cleaning</h1>
    <p class="tagline">Claeaning Services</p>
  </main>
</body>
</html>
```